Counselling business needs a DL brochure design ready for print next week!

My business is called Calm Harbour Counselling. My name is Megan Toller and I'm a qualified Psychotherapist based in Sydney, Australia.

I need a DL brochure to promote my business. I like the idea of possibly incorporating a leaf/leaves and/or the colour green in a sophisticated, understated way in the DL design. I have attached a leaf image for reference. I am looking for a simple, elegant design overall. Not too many fonts, something which is easy to read and captures people's interest.

I need a print ready design - something that my local instant printer can use easily. I need a print ready PDF and original files too for the printer. I am anticipating that the design will be A4 folded to DL as it needs to fit into standard dimension plastic DL stands at various locations.

My business is focussed upon helping people overcome difficulties such as grief or anxiety. I also work with people to help them plan their life adventures. My business is different from the average counselling business. For example, I give my clients a beautiful thick stock postcard at the end of every session with takeaway learnings and insights which they've uncovered. That way, they can reflect upon those discoveries and capitalise upon them.

I have an office in a local wellness centre. The brochure will be showcased at the centre and in local medical centres and shops. The aim is that new prospects will pick up the brochure and be prompted to call me for a counselling appointment.

I have attached copy for my DL brochure and a competitor's DL for reference. I'm not seeking to emulate the competitor, but I thought that it could be a useful reference - the competitor DL is clear and easy to read. I need my photo to be included in the brochure, adjacent to the information about my background. I have attached a reference photo for use as a positional - a full size image will need to be dropped in as part of this job by the winning designer.

I do not have a company logo at the moment, but I need my business name and contact details repeated several times in the DL.
Updates

Hello. Thank you for your designs. I am so pleased to have received them. I will be in touch in the next 24 hours. Best, Megan

Industry/Entity Type

Business

```html
<!DOCTYPE html>
<html lang="en">
<head>
<meta charset="utf-8">
<title>Calm Harbour Counselling – DL Brochure</title>
<link href="https://fonts.googleapis.com/css2?family=Montserrat:wght@600;700&family=Questrial&display=swap" rel="stylesheet">
<style>
:root{
  --green:#7ab829;
  --green-dark:#5c9a1c;
  --green-pale:#e3ecd6;
  --ink:#3d3d3d;
  --grey:#5a5a5a;
  --paper:#ffffff;
  --panel-tint:#f3f3f1;
  --backdrop:#e7e5e1;
}
*{margin:0;padding:0;box-sizing:border-box}
html,body{width:1200px;height:472px;overflow:hidden}
body{background:var(--backdrop);font-family:"Questrial",sans-serif;color:var(--grey);position:relative}
.sheet{position:absolute;background:var(--paper);box-shadow:0 1px 4px rgba(0,0,0,.18);overflow:hidden}
.sheet--outside{left:22px;top:22px;width:568px;height:402px}
.sheet--inside{left:610px;top:50px;width:568px;height:400px}
.panel{position:absolute;top:0;height:100%;width:190px}
.panel + .panel{border-left:1px solid #e2e2e2}
.abs{position:absolute}
.center{text-align:center}
.headline{font-family:"Montserrat",sans-serif;font-weight:700;color:var(--green)}
.brand{display:flex;align-items:center;gap:6px;font-family:"Montserrat",sans-serif;font-weight:700;color:var(--green);line-height:1.05;text-transform:uppercase;white-space:nowrap}
.brand__dot{flex:none;border-radius:50%;background:var(--green)}
.brand--white{color:#fff}
.brand--white .brand__dot{background:#fff}
.phone{font-family:"Montserrat",sans-serif;font-weight:700;color:var(--ink);display:flex;align-items:center;gap:4px;white-space:nowrap}
.contact-line{display:flex;align-items:center;gap:4px;font-size:8px;color:var(--grey);white-space:nowrap}
.photo{position:absolute}
.bodycopy{text-align:justify}
.cover-contacts{position:absolute;right:7px;display:flex;flex-direction:column;align-items:flex-end;gap:4px}
</style>
</head>
<body>

<section class="sheet sheet--outside">

  <div class="panel" style="left:0;background:var(--panel-tint)">
    <h2 class="headline abs center" style="left:0;width:190px;top:22px;font-size:13.5px;line-height:17px">DO YOU NEED<br>A POSITIVE CHANGE?</h2>
    <p class="abs" style="left:16px;top:61px;width:162px;font-size:10.3px;line-height:13.6px">DO YOU WISH You felt more joyful and fulfilled? You felt less stressed or overwhelmed? You coped better with life's challenges? You could break unhelpful habits? DO YOU IMAGINE Your relationships being closer? Your life being well balanced? Your goals being within reach? Your life being more adventurous?</p>
    <div class="brand abs" style="left:16px;top:206px;font-size:11.5px">
      <span class="brand__dot" style="width:28px;height:28px"></span>
      <span>Calm Harbour<br>Counselling</span>
    </div>
    <div class="photo" role="img" aria-label="Photo of a family walking together in a sunny green field" style="left:16px;top:246px;width:157px;height:104px;background:linear-gradient(180deg,#4f8fd6 0%,#a9cdf0 45%,#b8c66a 60%,#6f9a2e 100%)"></div>
    <div class="phone abs" style="left:0;width:190px;justify-content:center;top:362px;font-size:15.5px">
      <svg width="14" height="14" viewBox="0 0 24 24"><circle cx="12" cy="12" r="10.5" fill="none" stroke="#3d3d3d" stroke-width="2"/><path d="M8.5 7c.6-.5 1.3-.4 1.6.2l.9 1.7c.2.5.1 1-.3 1.3l-.6.5c.6 1.4 1.6 2.4 3 3l.5-.6c.3-.4.8-.5 1.3-.3l1.7.9c.6.3.7 1 .2 1.6-1 1.1-2.5 1.2-3.9.4-2.3-1.2-3.9-2.8-5.1-5.1-.7-1.4-.6-2.9.7-3.6z" fill="#3d3d3d"/></svg>
      604-555-0182
    </div>
    <div class="contact-line abs" style="left:0;width:190px;justify-content:center;top:385px;font-size:8.5px">
      <span style="width:6px;height:6px;border-radius:50%;background:var(--grey)"></span>www.calmharbourcounselling.com
    </div>
  </div>

  <div class="panel" style="left:190px;background:var(--paper)">
    <div class="abs" style="left:55px;top:112px;width:76px;height:76px;border-radius:50%;background:var(--green-pale)"></div>
    <p class="abs center" style="left:10px;width:170px;top:198px;font-family:'Montserrat',sans-serif;font-weight:600;font-size:12px;line-height:17px;color:var(--ink)">The power to create new possibilities is within you.</p>
    <p class="abs center" style="left:10px;width:170px;top:246px;font-family:'Montserrat',sans-serif;font-weight:600;font-size:11.5px;line-height:17px;color:var(--green)">You might just need<br>a helping hand</p>
  </div>

  <div class="panel" style="left:379px;width:189px;background:var(--paper)">
    <div class="brand abs" style="left:16px;top:24px;font-size:13px">
      <span class="brand__dot" style="width:30px;height:30px"></span>
      <span>Calm Harbour<br>Counselling</span>
    </div>
    <div class="photo" role="img" aria-label="Photo of a young woman with arms spread wide, enjoying the sun in a green meadow" style="left:0;top:112px;width:189px;height:194px;background:linear-gradient(160deg,#c9d9a0 0%,#9bbd5a 40%,#6f9a36 75%,#4e7a25 100%)"></div>
  </div>

  <svg class="abs" style="left:0;top:0" width="568" height="402" viewBox="0 0 568 402" aria-hidden="true">
    <path d="M196 0 C236 70 330 104 568 110 L568 118 C326 112 226 78 186 0 Z" fill="#dedede"/>
    <path d="M214 0 C250 62 340 92 568 96 L568 108 C336 104 238 72 202 0 Z" fill="var(--green)"/>
    <path d="M190 402 L190 392 C215 334 280 302 379 296 C450 292 520 298 568 306 L568 402 Z" fill="#ffffff"/>
    <path d="M190 392 C215 334 280 302 379 296 C450 292 520 298 568 306 L568 318 C520 310 450 304 379 308 C288 314 226 344 198 402 L190 402 Z" fill="var(--green)"/>
  </svg>

  <div class="brand abs" style="left:282px;top:322px;font-size:8.5px;gap:5px">
    <span class="brand__dot" style="width:16px;height:16px"></span>
    <span>Calm Harbour<br>Counselling</span>
  </div>
  <div class="cover-contacts" style="right:196px;top:348px">
    <div class="contact-line" style="font-size:7px">
      <svg width="7" height="9" viewBox="0 0 10 14"><path d="M5 0a5 5 0 0 0-5 5c0 3.6 5 9 5 9s5-5.4 5-9a5 5 0 0 0-5-5zm0 7a2 2 0 1 1 0-4 2 2 0 0 1 0 4z" fill="#5a5a5a"/></svg>
      210-1480 Willow Bend Road Fernvale
    </div>
    <div class="phone" style="font-size:10.5px;font-weight:600">
      <svg width="10" height="10" viewBox="0 0 24 24"><circle cx="12" cy="12" r="10.5" fill="none" stroke="#3d3d3d" stroke-width="2.4"/><path d="M8.5 7c.6-.5 1.3-.4 1.6.2l.9 1.7c.2.5.1 1-.3 1.3l-.6.5c.6 1.4 1.6 2.4 3 3l.5-.6c.3-.4.8-.5 1.3-.3l1.7.9c.6.3.7 1 .2 1.6-1 1.1-2.5 1.2-3.9.4-2.3-1.2-3.9-2.8-5.1-5.1-.7-1.4-.6-2.9.7-3.6z" fill="#3d3d3d"/></svg>
      604-555-0182
    </div>
    <div class="contact-line" style="font-size:7px">
      <svg width="8" height="6" viewBox="0 0 16 12"><rect x=".5" y=".5" width="15" height="11" fill="none" stroke="#5a5a5a"/><path d="M.5 .5 8 7l7.5-6.5" fill="none" stroke="#5a5a5a"/></svg>
      hello@calmharbourcounselling.com
    </div>
    <div class="contact-line" style="font-size:7px">
      <span style="width:5px;height:5px;border-radius:50%;background:var(--grey)"></span>www.calmharbourcounselling.com
    </div>
  </div>

  <p class="abs center" style="left:379px;width:189px;top:356px;font-family:'Montserrat',sans-serif;font-weight:600;font-size:11.5px;line-height:18px;color:var(--ink)">Overcome Difficulties and<br><span style="color:var(--green)">Make A Fresh Start</span></p>
</section>

<section class="sheet sheet--inside">

  <div class="panel" style="left:0">
    <div class="photo" role="img" aria-label="Close-up photo of a green leaf tip with a water drop falling into a rippling pool" style="left:0;top:0;width:190px;height:400px;background:linear-gradient(180deg,#5f9e28 0%,#8cc04a 22%,#d9e8c4 45%,#f4f7ee 62%,#bcd69a 78%,#6ba72e 100%)"></div>
    <div class="contact-line abs" style="left:24px;top:20px;color:#fff;font-size:9px">
      <svg width="9" height="7" viewBox="0 0 16 12"><rect x=".5" y=".5" width="15" height="11" fill="none" stroke="#fff"/><path d="M.5 .5 8 7l7.5-6.5" fill="none" stroke="#fff"/></svg>
      hello@calmharbourcounselling.com
    </div>
    <div class="phone abs" style="left:22px;top:36px;color:#fff;font-size:17px">
      <svg width="15" height="15" viewBox="0 0 24 24"><circle cx="12" cy="12" r="10.5" fill="none" stroke="#fff" stroke-width="2"/><path d="M8.5 7c.6-.5 1.3-.4 1.6.2l.9 1.7c.2.5.1 1-.3 1.3l-.6.5c.6 1.4 1.6 2.4 3 3l.5-.6c.3-.4.8-.5 1.3-.3l1.7.9c.6.3.7 1 .2 1.6-1 1.1-2.5 1.2-3.9.4-2.3-1.2-3.9-2.8-5.1-5.1-.7-1.4-.6-2.9.7-3.6z" fill="#fff"/></svg>
      604-555-0182
    </div>
    <div class="contact-line abs" style="left:24px;top:60px;color:#fff;font-size:9px">
      <span style="width:6px;height:6px;border-radius:50%;background:#fff"></span>www.calmharbourcounselling.com
    </div>
    <div class="brand brand--white abs" style="left:20px;top:350px;font-size:14px">
      <span class="brand__dot" style="width:32px;height:32px"></span>
      <span>Calm Harbour<br>Counselling</span>
    </div>
  </div>

  <div class="panel" style="left:190px;background:var(--paper)">
    <div class="brand abs" style="left:20px;top:22px;font-size:14px">
      <span class="brand__dot" style="width:32px;height:32px"></span>
      <span>Calm Harbour<br>Counselling</span>
    </div>
    <p class="bodycopy abs" style="left:16px;top:68px;width:160px;font-size:8.6px;line-height:9.85px">WE HELP...clients make significant, positive changes in their lives. We can help you shift current challenges, break unhelpful habits, and begin to experience life differently. Working together in a supportive, non-judgemental environment, we can help you start to build upon your strengths, gain greater awareness and understanding, develop helpful perspectives, and learn practical strategies and techniques. Bit by bit you can start to turn over a new leaf. With our help, discover new ways of dealing with challenges in your life, start to experience life more fully and joyfully, and THRIVE! At Calm Harbour Counselling, we help clients experiencing immediate and long term difficulties with: Depression Anxiety Grief and loss Trauma Interpersonal and relationship challenges Addiction (or third party addiction) Occupational challenges Adjustment to change Generalised dissatisfaction/disillusionment Self (esteem, identity, purpose, meaning) Identifying and achieving personal goals</p>
    <div class="contact-line abs" style="left:20px;top:340px;font-size:9px">
      <svg width="9" height="7" viewBox="0 0 16 12"><rect x=".5" y=".5" width="15" height="11" fill="none" stroke="#5a5a5a"/><path d="M.5 .5 8 7l7.5-6.5" fill="none" stroke="#5a5a5a"/></svg>
      hello@calmharbourcounselling.com
    </div>
    <div class="phone abs" style="left:18px;top:354px;font-size:17px">
      <svg width="15" height="15" viewBox="0 0 24 24"><circle cx="12" cy="12" r="10.5" fill="none" stroke="#3d3d3d" stroke-width="2"/><path d="M8.5 7c.6-.5 1.3-.4 1.6.2l.9 1.7c.2.5.1 1-.3 1.3l-.6.5c.6 1.4 1.6 2.4 3 3l.5-.6c.3-.4.8-.5 1.3-.3l1.7.9c.6.3.7 1 .2 1.6-1 1.1-2.5 1.2-3.9.4-2.3-1.2-3.9-2.8-5.1-5.1-.7-1.4-.6-2.9.7-3.6z" fill="#3d3d3d"/></svg>
      604-555-0182
    </div>
    <div class="contact-line abs" style="left:20px;top:377px;font-size:9px">
      <span style="width:6px;height:6px;border-radius:50%;background:var(--grey)"></span>www.calmharbourcounselling.com
    </div>
  </div>

  <div class="panel" style="left:379px;width:189px;background:var(--paper)">
    <div class="photo" role="img" aria-label="Portrait photo of the counsellor outdoors against green foliage" style="left:43px;top:22px;width:104px;height:103px;background:linear-gradient(180deg,#8fb04c 0%,#6e9434 55%,#4d6f3a 100%)"></div>
    <div class="abs" style="left:0;width:189px;top:138px;display:flex;justify-content:center;align-items:center;gap:6px">
      <span style="width:14px;height:14px;border-radius:50%;background:var(--green)"></span>
      <h3 class="headline" style="font-size:14px">MEGAN TOLLER</h3>
      <span style="width:14px;height:14px;border-radius:50%;background:var(--green)"></span>
    </div>
    <p class="abs center" style="left:10px;width:169px;top:160px;font-size:8.6px;line-height:10.5px;color:var(--ink)">Psychotherapist, Counsellor,<br>Life Coach B.A., G.Dip.<br>Counselling &amp; Psychotherapy</p>
    <p class="bodycopy abs" style="left:14px;top:200px;width:161px;font-size:7.15px;line-height:8.25px">Megan Toller is an accredited Psychotherapist and Counsellor. She has been providing individual, couple and group therapeutic services to clients since 2003. Megan works collaboratively and holistically with clients, drawing upon a wide variety of evidence-based therapeutic modalities. Whether you're in a difficult life situation seeking CBT strategies and Family System insights, or you're wanting to plan your next life adventure and develop Mindfulness practices, Megan can work closely with you to address current issues, devise and implement solutions-focused counselling strategies, and create opportunities for positive change. Whilst every Calm Harbour Counselling session with Megan is unique, you can expect to go on a journey of exploration, discovery, empowerment and change. It's an opportunity to make a fresh start and turn over a new leaf. To make an appointment or find out more about how Calm Harbour Counselling can help you, contact Megan Toller on 0400 555 017, or email yourname@calmharbourcounselling.com</p>
  </div>
</section>

</body>
</html>
```